Home Health Company Needs a Corporate Identity Package

We need a corporate identity package (see what it should include below) for a home health care company. The design should be professional, uncluttered, simple and created in Publisher (so that we can edit the design in the future, if necessary. )
We need the following created:
-Presentation folder
-Business card template (color, double sided)
-Letterhead
-Stationary
-postcard sized marketing piece (5.5" x 8.5", color, double sided)

Target Market(s)

We are in the business of supplying personal care aids for in home care. Our services are directed towards older, retired individuals with some disability or illness. However, we will be marketing to the children or relatives of our in home clients. We want our logo to emphasize our reliability and personalized services.

Industry/Entity Type

Home Health Care

Requirements
Must have
• The design should be professional, uncluttered, simple and created in Publisher (so that we can edit the design in the future, if necessary. )

```html
<!DOCTYPE html>
<html lang="en">
<head>
<meta charset="utf-8">
<title>Harbor Lane Care – Postcard</title>
<link href="https://fonts.googleapis.com/css2?family=Open+Sans:wght@400;600&display=swap" rel="stylesheet">
<style>
  :root {
    --backdrop: #4a4a4c;
    --card: #efefef;
    --card-back: #f2f2f2;
    --brand-blue: #4aaee0;
    --charcoal: #5a5558;
    --text-grey: #7a7a7a;
    --rule: #9a9a9a;
    --tpl-blue: #d6ecf8;
    --tpl-white: #ffffff;
    --tpl-grey: #858587;
  }
  * { margin: 0; padding: 0; box-sizing: border-box; }
  html, body { width: 1200px; height: 1000px; overflow: hidden; }
  body {
    background: var(--backdrop);
    font-family: "Open Sans", Arial, sans-serif;
    position: relative;
  }
  .card {
    position: absolute;
    width: 495px;
    height: 321px;
    box-shadow: 2px 3px 6px rgba(0,0,0,.35);
  }
  .card--back { left: 206px; top: 253px; background: var(--card-back); }
  .card--front { left: 506px; top: 77px; background: var(--card); }

  .brand-name {
    position: absolute;
    color: var(--brand-blue);
    font-weight: 600;
    line-height: 1.05;
    display: flex;
    align-items: center;
    gap: 8px;
  }
  .brand-name__dot {
    width: 22px; height: 22px; border-radius: 50%;
    background: var(--brand-blue);
    flex: none;
  }
  .card--front .brand-name { left: 74px; top: 72px; font-size: 30px; }
  .card--back .brand-name { left: 86px; top: 88px; font-size: 25px; }
  .card--back .brand-name__dot { width: 18px; height: 18px; }

  .front-bar { position: absolute; top: 210px; height: 12px; }
  .front-bar--dark { left: 0; width: 312px; background: var(--charcoal); }
  .front-bar--blue { left: 316px; right: 0; background: var(--brand-blue); }
  .front-band {
    position: absolute; left: 0; right: 0; top: 227px; bottom: 0;
    background: var(--charcoal);
  }

  .return-address {
    position: absolute; left: 0; width: 290px; top: 28px;
    text-align: center; font-size: 7.5px; color: var(--text-grey); line-height: 1.35;
  }
  .return-address .label { color: var(--brand-blue); font-weight: 600; }

  .address-lines { position: absolute; left: 26px; top: 164px; width: 232px; }
  .address-lines span {
    display: block; height: 23px; border-bottom: 1px solid var(--rule);
  }

  .mailing-template {
    position: absolute; left: 403px; top: 655px;
    width: 401px; height: 262px;
    background: linear-gradient(160deg, var(--tpl-grey) 0%, var(--tpl-blue) 30%, var(--tpl-blue) 60%, var(--tpl-white) 100%);
  }
</style>
</head>
<body>

  <section class="card card--back" aria-label="Postcard address side">
    <p class="return-address">
      P.O. Box 4417, Kestrel Bay NSW 2290, Australia<br>
      <span class="label">T:</span> +61 2 5550 1834 · <span class="label">E:</span> hello@harborlanecare.com
    </p>
    <div class="brand-name"><span class="brand-name__dot"></span>Harbor Lane<br>Care</div>
    <div class="address-lines"><span></span><span></span><span></span><span></span><span></span></div>
  </section>

  <section class="card card--front" aria-label="Postcard front">
    <div class="brand-name"><span class="brand-name__dot"></span>Harbor Lane<br>Care</div>
    <div class="front-bar front-bar--dark"></div>
    <div class="front-bar front-bar--blue"></div>
    <div class="front-band"></div>
  </section>

  <div class="mailing-template" role="img" aria-label="Technical layout diagram of the 8.5 by 5.5 inch postcard mailing side, showing bleed, trim and safe zones, return address, postage permit, address and barcode areas"></div>

</body>
</html>
```